Poster Design Project

The Alder Street Traders Association is a committee of business operators in Brighton (a wealthy, mature suburb located in inner-metro Melbourne in Victoria, Australia. Please note that this is not Alder Street, Richmond) who represent an upmarket Main Street precinct with a large number of boutique fashion clothing and accessories retailers.

The Association will be holding a fashion parade in Spring to increase visitation to the street and further develop the profile of the street as one of Melbourne’s most fashionable main street shopping strips.

This design project is to develop promotional posters scalable to (1600mm H x 1260mm W)

The target market for this project is estimated to be generally female fashion shoppers over the age of 30 years.

For the design outputs:
File Format: PDF print-ready *and* .EPS and/or PSD master (to allow for modification of event details as needed)
Colours: CMYK

A classy, up-market feel is desired for the design, and a consistent look and feel for all the project elements is required.
The copy for the poster and the ad is as follows:

(Quotation marks not to be included!)

"Fashion at the Kettle
A catwalk spectacular to eclipse all others

Don’t be left in the dark this spring- discover the hottest trends from top designers all available from the fabulous fashion boutiques of Alder Street at the heart of Brighton.

Then shop til you drop with special discounts only available to ticket holders.

When: Sunday 28 October 2012, 2pm

Where: Copper Kettle Hotel
84 Alder Street Brighton

Tickets: $25 (includes champagne on arrival)
Tickets are available from the Copper Kettle Hotel and participating Alder Street traders.

Numbers are strictly limited – buy a ticket now!

Proudly presented by Brighton Kestrel – Summit Cars together with the Copper Kettle Hotel and the Alder Street Traders Association."

Stock imagery of generic fashion parades/modelling is not to be used.

More abstract ideas such as ‘designer sketches’ are acceptable.
General graphic design which evokes an exciting, glamorous feel is desired.

Please incorporate the Sponsor Block of logos

Target Market(s)

Industry/Entity Type

Graphic Design

Requirements
Must have
• Event text as above.

Please incorporate the Sponsor Block of logos (file to be uploaded)

EPS and/or PSD file for modification
Should not have
• Stock imagery of generic fashion parades/modelling is not to be used.

```html
<!DOCTYPE html>
<html lang="en">
<head>
<meta charset="utf-8">
<title>Fashion at the Kettle</title>
<link href="https://fonts.googleapis.com/css2?family=Montserrat:wght@600;700;800;900&display=swap" rel="stylesheet">
<style>
  :root {
    --bg-light: #d2d2d2;
    --bg-mid: #a9a9a9;
    --bg-dark: #7c7c7c;
    --red: rgba(150, 18, 24, 0.92);
    --red-band: rgba(160, 22, 28, 0.88);
    --panel: rgba(236, 236, 236, 0.94);
    --ink: #121212;
    --band-text: rgba(232, 226, 226, 0.85);
    --footer-ink: #2a2a2a;
  }
  * { box-sizing: border-box; margin: 0; padding: 0; }
  html, body { width: 848px; height: 1200px; overflow: hidden; }
  body { font-family: "Montserrat", Arial, sans-serif; color: var(--ink); }

  .poster { position: relative; width: 848px; height: 1200px; overflow: hidden;
    background: radial-gradient(ellipse at 50% 40%, var(--bg-light) 0%, var(--bg-mid) 55%, var(--bg-dark) 100%); }

  .backdrop-figure { position: absolute; left: 250px; top: 40px; width: 360px; height: 1080px;
    background: radial-gradient(ellipse at 50% 30%, rgba(90,90,90,0.55) 0%, rgba(120,120,120,0.25) 45%, rgba(160,160,160,0) 72%);
    filter: blur(10px); }

  /* Title block */
  .title-frame { position: absolute; left: 97px; top: 190px; width: 594px; height: 210px;
    background: var(--red); transform: rotate(-1.5deg); }
  .title-box { position: absolute; left: 16px; top: 14px; width: 556px; height: 160px; background: var(--panel);
    padding: 12px 22px; }
  .title { font-weight: 800; font-size: 60px; line-height: 0.98; letter-spacing: 1px; text-transform: uppercase; }
  .tagline { font-weight: 700; font-size: 13px; letter-spacing: 2.5px; text-transform: uppercase; margin-top: 6px; }

  /* Details block (sits beneath the band) */
  .details-frame { position: absolute; left: 150px; top: 530px; width: 610px; height: 530px;
    background: var(--red); transform: rotate(-3deg); }
  .box { position: absolute; background: var(--panel); text-transform: uppercase; font-weight: 800; }
  .discounts { left: 20px; top: 72px; width: 570px; height: 108px; padding: 12px 18px;
    font-size: 22px; line-height: 1.2; letter-spacing: 2px; }
  .price { left: 20px; top: 192px; width: 570px; height: 38px; padding: 8px 14px;
    font-size: 17px; letter-spacing: 1.5px; }
  .availability { left: 20px; top: 242px; width: 570px; height: 120px; padding: 10px 14px;
    font-size: 16px; line-height: 1.3; letter-spacing: 2px; }
  .availability .small { font-size: 14px; }
  .buy { display: block; text-align: right; font-size: 24px; letter-spacing: 1.5px; margin-top: 4px; padding-right: 6px; }
  .date { left: 20px; top: 376px; width: 172px; height: 144px; padding: 6px 12px;
    font-size: 44px; line-height: 1.0; }
  .venue { left: 204px; top: 376px; width: 386px; height: 120px; padding: 12px 12px;
    font-size: 27px; line-height: 1.12; letter-spacing: 0.5px; }

  /* Copy band (over both blocks) */
  .intro-band { position: absolute; left: -40px; top: 372px; width: 940px; height: 190px;
    background: var(--red-band); transform: rotate(-6deg); padding: 16px 70px 0 76px; }
  .intro { color: var(--band-text); font-weight: 800; font-size: 28px; line-height: 1.16; letter-spacing: 3px;
    text-transform: uppercase; text-align: justify; text-align-last: left; width: 790px; }

  /* Sponsors */
  .sponsors { position: absolute; left: 0; top: 1110px; width: 848px; }
  .credit { font-weight: 700; font-size: 8px; letter-spacing: 0.5px; text-transform: uppercase; color: var(--footer-ink);
    line-height: 1.4; width: 300px; margin: 0 0 0 264px; text-align: left; }
  .sponsor-row { display: flex; justify-content: center; align-items: center; gap: 26px; margin-top: 18px; }
  .sponsor { font-weight: 700; font-size: 13px; color: var(--footer-ink); display: flex; align-items: center; gap: 6px; }
  .sponsor .dot { width: 22px; height: 22px; border: 1.5px solid var(--footer-ink); border-radius: 50%; }
</style>
</head>
<body>
<main class="poster">
  <div class="backdrop-figure" role="img" aria-label="Soft, blurred silhouette of a figure in grey tones behind the text"></div>

  <section class="title-frame">
    <div class="title-box">
      <h1 class="title">Fashion at<br>the Kettle</h1>
      <p class="tagline">A catwalk spectacular to eclipse all others</p>
    </div>
  </section>

  <section class="details-frame">
    <p class="box discounts">Then shop til you drop<br>with special discounts only<br>available to ticket holders.</p>
    <p class="box price">Tickets $25 (with champagne on arrival)</p>
    <div class="box availability">
      <p>Tickets are available from the Copper<br>Kettle Hotel and participating Alder Street<br>traders. <span class="small">Numbers are strictly limited</span></p>
      <span class="buy">Buy a ticket now!</span>
    </div>
    <p class="box date">Sun<br>28.10<br>2 PM</p>
    <p class="box venue">Copper Kettle Hotel<br>84 Alder St.<br>Brighton, Vic</p>
  </section>

  <section class="intro-band">
    <p class="intro">Don’t be left in the dark this spring, discover the hottest trends from top designers all available from the fabulous fashion boutiques of Alder Street at the heart of Brighton.</p>
  </section>

  <footer class="sponsors">
    <p class="credit">Proudly presented by Brighton Kestrel – Summit Cars together with the Copper Kettle Hotel and the Alder Street Traders Association.</p>
    <div class="sponsor-row">
      <span class="sponsor">Kestrel</span>
      <span class="sponsor">Bayside Motors</span>
      <span class="sponsor">Summit Cars</span>
      <span class="sponsor"><span class="dot"></span>Copper Kettle</span>
    </div>
  </footer>
</main>
</body>
</html>
```